We need a flyer (size Din A4, folded, see image).
Attached you will find the content with a rough arrangement.
The inner part will contain some Q&A, we have sketched two possible arrangements of the content.
We are looking for a professional design and a good, clean layout.
Maybe you have some ideas how to arrange the content in a smarter way, we are open for suggestions.
The draft contains no images. It would be good to have an explaining image at least on the front of the flyer.
Attached you will find some stock photos we are using on our website, but you can also propose your own images.
If useful, here is our webpage:
https://vorn-strom.de/
and the landing page for the offering
https://vorn-strom. en/charging-solutions-for-house-management-and-routes/
(this landing page is not professionally designed, so feel free to create a better design for the flyer)
Our target group are real estate managers/facility managers of larger apartment buildings.
The offering is: full-serviced solutions for charging infrastructure for electric cars at the parking lots for residents.
Please do not hesitate to contact me, if you need further information.
Target Market(s)
Professionals in real estate management, facility management
Industry/Entity Type
charging infrastructures for electric cars, focus: appartment buildings

```html
<!DOCTYPE html>
<html lang="de">
<head>
<meta charset="utf-8">
<title>vorn-strom Flyer</title>
<link href="https://fonts.googleapis.com/css2?family=Montserrat:wght@400;500;600;700;800&display=swap" rel="stylesheet">
<style>
:root{
  --bg:#e4e5e6;
  --navy:#181b2b;
  --navy-2:#232738;
  --magenta:#e6149a;
  --violet:#9b3fd0;
  --ink:#1e1f29;
  --muted:#5b5e6b;
  --white:#ffffff;
  --row:#f4f4f6;
  --line:#d9dae0;
}
*{box-sizing:border-box;margin:0;padding:0}
html,body{width:1200px;height:4000px;overflow:hidden;background:var(--bg);font-family:"Montserrat",Arial,sans-serif;color:var(--ink)}
.spread{position:absolute;left:120px;width:960px;height:679px;background:var(--white);box-shadow:0 10px 24px rgba(0,0,0,.25);display:flex}
.spread--outer{top:1241px}
.spread--inner{top:2080px}
.panel{position:relative;width:320px;height:100%;overflow:hidden}
.photo{position:absolute;left:0;width:100%}
.wordmark{display:flex;align-items:center;justify-content:center;gap:8px;font-weight:600;font-size:19px}
.wordmark i{width:12px;height:12px;border-radius:50%;background:var(--magenta);display:block}
/* outer left */
.benefits{position:absolute;top:236px;left:0;width:100%;height:176px;background:linear-gradient(90deg,var(--magenta),var(--violet));color:var(--white);padding:26px 34px}
.benefits h2{font-size:12.5px;font-weight:700;line-height:1.5;text-transform:uppercase;margin-bottom:6px}
.ticks li{list-style:none;font-size:13px;font-weight:500;line-height:26px;display:flex;align-items:center;gap:7px}
.ticks svg{width:11px;height:11px}
.features{position:absolute;top:412px;left:0;width:100%}
.feature{height:89px;border-bottom:3px solid var(--line);display:flex;align-items:center;padding:0 30px}
.feature p{border-left:2px solid var(--ink);padding-left:8px;font-size:10.5px;font-weight:700;line-height:1.3}
/* outer middle */
.panel--contact{background:var(--navy);color:var(--white);text-align:center}
.panel--contact .wordmark{position:absolute;top:210px;width:100%;color:var(--white)}
.cta{position:absolute;top:300px;width:100%;font-size:14px;font-weight:700;line-height:1.45;text-transform:uppercase}
.pill{position:absolute;left:50%;transform:translateX(-50%);width:204px;height:24px;border-radius:12px;background:var(--magenta);font-size:13px;font-weight:700;line-height:24px}
.or{position:absolute;top:397px;width:100%;font-size:13px;font-weight:700}
.about{position:absolute;top:462px;left:30px;right:30px;font-size:8.5px;line-height:1.4;color:#c9cbd6}
.address-box{position:absolute;top:502px;left:49px;width:222px;height:150px;border:1px solid #cfd1da;font-size:8px;line-height:1.45;color:#d7d8e0;padding-top:14px}
.address-box div{margin-bottom:10px}
.address-box svg{width:11px;height:13px;display:block;margin:0 auto 3px}
/* outer right */
.brandhead{position:absolute;top:0;left:0;width:100%;height:95px;background:var(--white)}
.brandhead .wordmark{position:absolute;top:38px;width:100%}
.panel--cover{background:var(--white);text-align:center}
.lead{position:absolute;top:118px;left:24px;right:24px;font-size:9px;line-height:1.45;color:var(--ink)}
.claim{position:absolute;top:155px;left:12px;right:20px;height:70px;background:linear-gradient(90deg,var(--magenta),var(--violet));color:var(--white);font-size:10px;font-weight:600;line-height:20px;padding-top:6px}
.cover-text{position:absolute;top:590px;left:26px;right:26px;font-size:8.5px;line-height:1.45;color:var(--muted)}
.cover-text p{margin-bottom:8px}
/* inner */
.qa{width:640px;height:100%;position:relative;background:var(--white)}
.qa-head{position:absolute;top:0;left:0;width:100%;height:76px;border-bottom:2px solid var(--violet)}
.qa-head h3{position:absolute;top:22px;font-size:13px;font-weight:700;color:var(--magenta);text-transform:uppercase;line-height:1.25}
.qa-head .q{left:52px;border-left:2px solid var(--violet);padding-left:20px;top:14px;padding-top:8px;height:62px}
.qa-head .a{left:354px}
.rows{position:absolute;top:88px;left:30px;width:580px}
.row{display:flex;align-items:center;background:var(--row);margin-bottom:8px;border-bottom:2px solid var(--line)}
.row .question{width:190px;padding:0 0 0 20px;font-size:9.5px;font-weight:600;line-height:1.3}
.row .arrow{width:80px;display:flex;justify-content:center}
.row .arrow svg{width:48px;height:36px}
.row .answer{flex:1;padding:8px 12px 8px 0;font-size:8.5px;font-weight:600;line-height:1.35}
.row .answer p+p{margin-top:6px}
.row--1{height:108px}.row--2{height:64px}.row--3{height:108px}.row--4{height:74px}.row--5{height:118px}.row--6{height:62px}
.qa-band{position:absolute;left:0;bottom:0;width:100%;height:225px;background:linear-gradient(90deg,var(--magenta) 0,var(--magenta) 22px,transparent 22px),linear-gradient(0deg,var(--magenta) 0,var(--magenta) 22px,transparent 22px);z-index:0}
.rows{z-index:1}
.panel--steps{background:var(--navy);color:var(--white)}
.steps-title{position:absolute;top:30px;left:38px;font-size:13px;font-weight:700;color:var(--magenta);line-height:1.25;text-transform:uppercase}
.steps{position:absolute;top:108px;left:36px;right:20px}
.steps::before{content:"";position:absolute;left:15px;top:20px;height:240px;width:2px;background:var(--magenta)}
.step{position:relative;display:flex;gap:18px;margin-bottom:22px}
.step-icon{width:32px;height:32px;border-radius:50%;border:2px solid var(--magenta);background:var(--navy);flex:none;display:flex;align-items:center;justify-content:center}
.step-icon i{width:12px;height:12px;border-radius:50%;background:var(--violet);display:block}
.step h4{font-size:11px;font-weight:700;margin:6px 0 6px}
.step li{list-style:none;font-size:8px;color:#c9cbd6;line-height:1.55;padding-left:12px;position:relative}
.step li::before{content:"";position:absolute;left:0;top:3px;width:6px;height:6px;border-radius:50%;border:1px solid var(--magenta)}
</style>
</head>
<body>

<!-- Outer side -->
<section class="spread spread--outer">
  <div class="panel panel--benefits">
    <div class="photo" style="top:0;height:236px;background:linear-gradient(135deg,#dfe4ec,#3a4f86 55%,#1b2238)" role="img" aria-label="Ladestecker eines Elektroautos an der Ladesäule, Nahaufnahme"></div>
    <div class="benefits">
      <h2>Bieten Sie Ihren Bewohnern Lademöglichkeiten für ihre Elektrofahrzeuge –</h2>
      <ul class="ticks">
        <li><svg viewBox="0 0 12 12"><circle cx="6" cy="6" r="5" fill="none" stroke="#fff"/><path d="M3.5 6l1.8 1.8L8.6 4.4" fill="none" stroke="#fff"/></svg>Einfach</li>
        <li><svg viewBox="0 0 12 12"><circle cx="6" cy="6" r="5" fill="none" stroke="#fff"/><path d="M3.5 6l1.8 1.8L8.6 4.4" fill="none" stroke="#fff"/></svg>Unkompliziert</li>
        <li><svg viewBox="0 0 12 12"><circle cx="6" cy="6" r="5" fill="none" stroke="#fff"/><path d="M3.5 6l1.8 1.8L8.6 4.4" fill="none" stroke="#fff"/></svg>Zukunftsfähig</li>
      </ul>
    </div>
    <div class="features">
      <div class="feature"><p>Zukunftsfähig durch flexibles<br>Abrechnungsmodell für verschiedene<br>Einsatzmöglichkeiten.</p></div>
      <div class="feature"><p>Leichter, schneller Einstieg in das<br>Thema, unkomplizierte und<br>professionelle Abwicklung</p></div>
      <div class="feature"><p>Aufbau und Betrieb von Ladelösungen<br>speziell für Hausverwaltungen<br>und WEGs</p></div>
    </div>
  </div>

  <div class="panel panel--contact">
    <div class="photo" style="top:0;height:200px;background:linear-gradient(180deg,#3b3f4e,var(--navy))" role="img" aria-label="Elektroauto beim Laden in einer dunklen Garage"></div>
    <div class="wordmark"><i></i>vorn-strom.de</div>
    <p class="cta">Jetzt Beratungsgespräch<br>anfordern unter:</p>
    <div class="pill" style="top:353px">https://vorn-strom.de/WEG</div>
    <p class="or">oder</p>
    <div class="pill" style="top:420px">0800 / 123 45 67</div>
    <p class="about">Als Anbieter von Full-Service-Lösungen ermöglicht vorn-strom eine für Immobilienbesitzer/-verwalter einfache und ausbaubare Lösung, die alle Bereiche abdeckt.</p>
    <div class="address-box">
      <div><svg viewBox="0 0 12 14"><path d="M6 13C2 8 1 6.5 1 5a5 5 0 0110 0c0 1.5-1 3-5 8z" fill="#e6149a"/><circle cx="6" cy="5" r="1.8" fill="#181b2b"/></svg>vorn-strom GmbH, Lindenweg 4<br>80331 Beispielstadt</div>
      <div><svg viewBox="0 0 12 14"><path d="M6 13C2 8 1 6.5 1 5a5 5 0 0110 0c0 1.5-1 3-5 8z" fill="#e6149a"/><circle cx="6" cy="5" r="1.8" fill="#181b2b"/></svg>HRB 000000, Amtsgericht Beispielstadt<br>Geschäftsführung: Mara Velden</div>
      <div><svg viewBox="0 0 12 14"><path d="M6 13C2 8 1 6.5 1 5a5 5 0 0110 0c0 1.5-1 3-5 8z" fill="#e6149a"/><circle cx="6" cy="5" r="1.8" fill="#181b2b"/></svg>vorn-strom GmbH, Lindenweg 4<br>80331 Beispielstadt</div>
    </div>
  </div>

  <div class="panel panel--cover">
    <div class="photo" style="top:95px;height:480px;background:linear-gradient(180deg,#8a8d94,#4a4d55 40%,#2a2c33)" role="img" aria-label="Dunkles Elektroauto in einer Tiefgarage an einer Wallbox"></div>
    <div class="brandhead"><div class="wordmark"><i></i>vorn-strom.de</div></div>
    <div class="lead" style="top:102px;background:var(--white);padding:10px 0;left:0;right:0">Bauträger und Hausverwaltungen/WEGs, die einfach<br>zukunftsfähige Ladelösungen für ihre Stellplätze benötigen</div>
    <div class="claim">Flexible Ladeinfrastrukturen für die Elektromobilität<br>für Mieter und Eigentümer<br>einfach, unkompliziert und zukunftsfähig</div>
    <div class="photo" style="top:575px;height:104px;background:var(--white)"></div>
    <div class="cover-text">
      <p>Hausverwaltungen werden von Mietern und Eigentümern immer öfter konfrontiert mit dem Wunsch nach Lademöglichkeiten für die Bewohner.</p>
      <p>Zudem verlangt das neue Gebäude-Elektromobilitätsinfrastruktur-Gesetz (GEIG) den Ausbau der Ladeinfrastruktur bei der Renovierung der TG.</p>
    </div>
  </div>
</section>

<!-- Inner side -->
<section class="spread spread--inner">
  <div class="qa">
    <div class="qa-band"></div>
    <div class="qa-head">
      <h3 class="q">Problem /<br>Fragestellung</h3>
      <h3 class="a">Der Lösungsansatz<br>von vorn-strom</h3>
    </div>
    <div class="rows">
      <div class="row row--1"><p class="question">Ein Bewohner will eine Wallbox – was tun?</p><div class="arrow"><svg viewBox="0 0 48 36"><path d="M0 12h28V2l20 16-20 16V24H0z" fill="#181b2b"/></svg></div><div class="answer"><p>Mieter/Eigentümer hat nach WoMoG Anspruch auf eine Wallbox.</p><p>Die Hausverwaltung darf den Wunsch nicht verhindern, darf aber – und sollte – Vorgaben machen, um eine nachhaltige Gesamtlösung sicherzustellen.</p><p>vorn-strom liefert diese Vorgaben, damit Installation und weiterer Ausbau geordnet erfolgen kann.</p></div></div>
      <div class="row row--2"><p class="question">Der Stromanschluss reicht nicht, wenn alle Bewohner eine Wallbox wollen!</p><div class="arrow"><svg viewBox="0 0 48 36"><path d="M0 12h28V2l20 16-20 16V24H0z" fill="#181b2b"/></svg></div><div class="answer"><p>Mit Hilfe des Last-Managements von vorn-strom lässt sich die verfügbare Strom-Kapazität intelligent steuern, so dass der Hausanschluss in der Regel langfristig ausreicht.</p></div></div>
      <div class="row row--3"><p class="question">Sind die Vorabprüfung und der Einbau von Ladeinfrastruktur teuer? Wie überzeugt man die WEG von den Kosten?</p><div class="arrow"><svg viewBox="0 0 48 36"><path d="M0 12h28V2l20 16-20 16V24H0z" fill="#181b2b"/></svg></div><div class="answer"><p>Bei der Lösung von vorn-strom werden nur aktuell benötigte Wallboxen aufgebaut – erforderliche Investitionen erfolgen schrittweise nach Bedarf.</p><p>Mit dem optionalen Mietmodell entstehen der WEG keine oder nur geringe Kosten, hier können die Kosten größtenteils auf die Nutzer der Wallboxen verlagert werden.</p></div></div>
      <div class="row row--4"><p class="question">Die Bewohner haben keine fest zugeordneten Stellplätze</p><div class="arrow"><svg viewBox="0 0 48 36"><path d="M0 12h28V2l20 16-20 16V24H0z" fill="#181b2b"/></svg></div><div class="answer"><p>Der Anschluss an den Wohnungszähler des jeweiligen Mieters/Eigentümers ist nicht notwendig.</p><p>vorn-strom rechnet auf Wunsch mit jedem Mieter direkt dessen Ladestromverbrauch ab.</p></div></div>
      <div class="row row--5"><p class="question">Wer kann helfen, eine professionelle und zukunftsfähige Ladeinfrastruktur zu entwickeln?</p><div class="arrow"><svg viewBox="0 0 48 36"><path d="M0 12h28V2l20 16-20 16V24H0z" fill="#181b2b"/></svg></div><div class="answer"><p>vorn-strom ist Spezialist für Ladeinfrastruktur, und kennt sich neben der speziellen technischen Lösungen auch mit rechtlichen Fragestellungen und Abrechnungslösungen aus.</p><p>Neben der Umsetzung unterstützt vorn-strom die Hausverwaltungen bei technischen und juristischen Fragen, um zusammen mit der WEG eine optimale Lösung aufzubauen.</p></div></div>
      <div class="row row--6"><p class="question">Bei uns wurden bereits Wallboxen von einzelnen Mietern installiert, was nun?</p><div class="arrow"><svg viewBox="0 0 48 36"><path d="M0 12h28V2l20 16-20 16V24H0z" fill="#181b2b"/></svg></div><div class="answer"><p>In vielen Fällen kann Hardware anderer Hersteller in die Abrechnungslösung von vorn-strom integriert werden.</p></div></div>
    </div>
  </div>

  <div class="panel panel--steps">
    <h3 class="steps-title">Die Schritte zur<br>Ladeinfrastruktur<br>in Ihrem Objekt:</h3>
    <div class="steps">
      <div class="step"><div class="step-icon"><i></i></div><div><h4>ERSTPRÜFUNG</h4><ul><li>Machbarkeitsprüfung</li><li>Abschätzung, Planung nächster Schritte</li></ul></div></div>
      <div class="step"><div class="step-icon"><i></i></div><div><h4>KONZEPTION</h4><ul><li>Planung der Anlage</li><li>Abstimmung Netzbetreiber</li><li>Kostenkalkulation</li></ul></div></div>
      <div class="step"><div class="step-icon"><i></i></div><div><h4>INSTALLATION</h4><ul><li>Installation von Verkabelung und Elektrotechnik</li><li>Installation der Wallboxen</li><li>Setup der Abrechnungssysteme</li></ul></div></div>
      <div class="step"><div class="step-icon"><i></i></div><div><h4>BETRIEB</h4><ul><li>Technischer Betrieb</li><li>Abrechnung</li><li>Regelmäßige Wartung (DGUV3)</li><li>Anmeldung und Verwaltung neuer Nutzer</li></ul></div></div>
    </div>
    <div class="photo" style="top:450px;height:229px;background:linear-gradient(90deg,#d9c9bf,#8d7a70 45%,#cfd0cc)" role="img" aria-label="Ladekabel an einem Elektroauto, im Hintergrund eine Person an der Garage"></div>
  </div>
</section>

</body>
</html>
```